First Aid Training business needs business card design

We would like a double sided business card designed for a first aid training business - Brindlewood First Aid. We provide first aid training and , WHS (work, health and safety) training.

The attached word document contains the key information we would like on each side of the business card.

Final design needs to be delivered in print ready format, along with the original file.

```html
<!DOCTYPE html>
<html lang="en">
<head>
<meta charset="utf-8">
<title>Brindlewood First Aid – Business Card</title>
<link rel="stylesheet" href="https://fonts.googleapis.com/css2?family=Montserrat:wght@400;500;600;700;800&display=swap">
<style>
  :root {
    --bg: #eeeeee;
    --paper: #ffffff;
    --ink: #111111;
    --red: #e1262c;
    --grey: #8a8a8a;
    --light: #f4f4f4;
  }
  html, body {
    margin: 0;
    width: 1200px;
    height: 900px;
    overflow: hidden;
    background: var(--bg);
    font-family: "Montserrat", sans-serif;
  }
  .canvas {
    position: relative;
    width: 1200px;
    height: 900px;
  }
  .card {
    position: absolute;
    left: 340px;
    width: 520px;
    height: 300px;
    box-shadow: 0 8px 24px rgba(0,0,0,0.12);
  }
  .card--front { top: 110px; }
  .card--back { top: 490px; }
  .card svg { display: block; }
  .brand-name { font-weight: 800; fill: var(--ink); letter-spacing: 1px; }
  .brand-sub { font-weight: 600; fill: var(--ink); letter-spacing: 1.5px; }
  .tagline-lead { font-weight: 700; fill: var(--paper); }
  .tagline { font-weight: 500; fill: var(--paper); }
  .holder-name { font-weight: 800; fill: var(--paper); letter-spacing: 3px; }
  .contact { font-weight: 500; fill: var(--ink); letter-spacing: 0.5px; }
</style>
</head>
<body>
<div class="canvas">

  <!-- Front of card -->
  <div class="card card--front">
    <svg width="520" height="300" viewBox="0 0 520 300" xmlns="http://www.w3.org/2000/svg">
      <rect class="card-paper" width="520" height="300" fill="var(--paper)"/>
      <path class="band-accent" d="M0,100 Q300,180 520,290" fill="none" stroke="var(--red)" stroke-width="3"/>
      <path class="band-dark" d="M0,110 Q300,190 520,300 L0,300 Z" fill="var(--ink)"/>

      <g class="brand">
        <circle cx="196" cy="70" r="22" fill="var(--red)"/>
        <text class="brand-name" x="230" y="72" font-size="26">BRINDLEWOOD</text>
        <text class="brand-sub" x="231" y="94" font-size="13">FIRST AID TRAINING</text>
      </g>

      <g class="tagline-block" text-anchor="middle">
        <text class="tagline-lead" x="190" y="236" font-size="13">Onsite Training – We can come to you</text>
        <text class="tagline" x="190" y="258" font-size="10.5">Time efficient  |  Cost effective  |  Minimise downtime for your team</text>
        <text class="tagline" x="190" y="278" font-size="10.5">First Aid Training  |  WHS Training</text>
      </g>
    </svg>
  </div>

  <!-- Back of card -->
  <div class="card card--back">
    <svg width="520" height="300" viewBox="0 0 520 300" xmlns="http://www.w3.org/2000/svg">
      <rect class="card-paper" width="520" height="300" fill="var(--paper)"/>
      <path class="band-line" d="M0,64 Q300,72 520,162" fill="none" stroke="var(--ink)" stroke-width="4"/>
      <path class="band-red" d="M0,0 H520 V150 Q300,62 0,58 Z" fill="var(--red)"/>
      <text class="holder-name" x="270" y="70" font-size="24" text-anchor="middle">DANIEL MARSH</text>

      <g class="contacts">
        <g class="contact-row">
          <circle cx="34" cy="150" r="8" fill="none" stroke="var(--red)" stroke-width="1.8"/>
          <path d="M30.5,146 q1,-1 2,0 l1,2 q-1,1 0,2 l1.5,1.5 q1,1 2,0 l2,1 q1,1 0,2 q-3,2 -6,-1 q-3,-3 -2.5,-7.5z" fill="var(--ink)"/>
          <text class="contact" x="50" y="155" font-size="13">0491 570 238</text>
        </g>
        <g class="contact-row">
          <circle cx="34" cy="176" r="8" fill="none" stroke="var(--red)" stroke-width="1.8"/>
          <rect x="29" y="172.5" width="10" height="7" fill="none" stroke="var(--ink)" stroke-width="1.3"/>
          <path d="M29,173 L34,177 L39,173" fill="none" stroke="var(--ink)" stroke-width="1.3"/>
          <text class="contact" x="50" y="181" font-size="13">HELP@BRINDLEWOODFIRSTAID.COM.AU</text>
        </g>
        <g class="contact-row">
          <circle cx="34" cy="202" r="8" fill="none" stroke="var(--red)" stroke-width="1.8"/>
          <circle cx="34" cy="202" r="4.5" fill="none" stroke="var(--ink)" stroke-width="1.2"/>
          <path d="M29.5,202 H38.5 M34,197.5 V206.5" stroke="var(--ink)" stroke-width="1"/>
          <text class="contact" x="50" y="207" font-size="13">WWW.BRINDLEWOODFIRSTAID.COM.AU</text>
        </g>
      </g>

      <g class="brand">
        <circle cx="318" cy="262" r="14" fill="var(--red)"/>
        <text class="brand-name" x="340" y="269" font-size="17" letter-spacing="0.5">BRINDLEWOOD</text>
      </g>
    </svg>
  </div>

</div>
</body>
</html>
```